Power point Presentation Template 2

I am looking a professionally designed Powerpoint Presentation template for my company. We are Information Technology Company. I have attached the Logo. The Logo will also give an indication of which colours to be used in the design.

Target Market(s)

Information and Communication Technology

Requirements
Must have
• All ideas welcomed
Nice to have
• Professional Look and Feel

```html
<!DOCTYPE html>
<html lang="en">
<head>
<meta charset="utf-8">
<title>Nexora presentation template</title>
<link href="https://fonts.googleapis.com/css2?family=Open+Sans:wght@400;600;700;800&display=swap" rel="stylesheet">
<style>
:root{
  --orange:#f47a00;
  --orange-soft:#f7953a;
  --yellow:#ffb400;
  --dark:#2b2b2b;
  --ink:#222;
  --muted:#666;
  --line:#cfcfcf;
  --page:#e6e6e6;
  --white:#fff;
}
*{box-sizing:border-box;margin:0;padding:0}
html,body{width:882px;height:1200px;overflow:hidden;background:var(--page);font-family:"Open Sans",Arial,sans-serif;color:var(--ink)}
.board{position:relative;width:882px;height:1200px}
.slide{position:absolute;width:278px;height:156px;background:var(--white);overflow:hidden}
.c1{left:11px}.c2{left:298px}.c3{left:585px}
.r1{top:11px}.r2{top:180px}.r3{top:349px}.r4{top:518px}.r5{top:688px}.r6{top:857px}.r7{top:1026px}
.abs{position:absolute}
.foot{position:absolute;left:0;bottom:0;width:100%;height:8px;background:var(--orange)}
.pg{position:absolute;right:0;bottom:0;width:14px;height:14px}
.pg svg{display:block}
.pg span{position:absolute;right:2px;bottom:1px;font-size:3.5px;color:#fff;font-weight:700}
.mark{position:absolute;right:6px;top:6px;display:flex;align-items:center;gap:2px;font-weight:800;font-size:6.5px;color:var(--orange);letter-spacing:.2px}
.mark i{display:block;width:5px;height:5px;border-radius:50%;background:var(--orange)}
.title{position:absolute;left:0;width:100%;text-align:center;font-size:13.5px;font-weight:400;color:var(--ink)}
.t{font-size:3.2px;line-height:1.45;color:var(--muted)}
.tw{font-size:3.2px;line-height:1.45;color:#fff}
.photo{position:absolute}
.brand{font-weight:800;color:var(--orange);letter-spacing:1px}
.ico{position:absolute;display:flex;align-items:center;justify-content:center;border-radius:50%}
</style>
</head>
<body>
<div class="board">

<!-- 1 cover -->
<section class="slide c1 r1">
  <div class="photo" role="img" aria-label="Greyscale photo of hands typing on a laptop with charts" style="inset:0;background:linear-gradient(135deg,#dcdcdc,#f2f2f2 45%,#bdbdbd)"></div>
  <div class="abs" style="left:0;top:41px;width:278px;height:65px;background:rgba(255,255,255,.85)"></div>
  <div class="abs brand" style="left:22px;top:55px;font-size:28px;display:flex;align-items:center;gap:6px"><i style="display:block;width:16px;height:16px;border-radius:50%;background:var(--orange)"></i>NEXORA</div>
  <div class="foot"></div>
</section>

<!-- 2 cover alt -->
<section class="slide c2 r1">
  <div class="photo" role="img" aria-label="Photo of a hand touching floating communication icons" style="inset:0;background:linear-gradient(135deg,#8fb0d4,#d7e4f2 50%,#6f8fb8)"></div>
  <div class="abs" style="left:10px;top:9px;width:258px;height:138px;background:rgba(235,242,250,.7)"></div>
  <div class="abs brand" style="left:75px;top:66px;font-size:20px;display:flex;align-items:center;gap:4px"><i style="display:block;width:11px;height:11px;border-radius:50%;background:var(--orange)"></i>NEXORA</div>
</section>

<!-- 3 section -->
<section class="slide c3 r1">
  <div class="photo" role="img" aria-label="Photo of a glowing golden circuit board" style="inset:0;background:radial-gradient(circle at 55% 60%,#8a6a1e,#2a2a1a 55%,#0e1a26)"></div>
  <div class="abs" style="left:32px;top:41px;width:75px;height:75px;background:var(--orange)"></div>
  <div class="abs" style="left:107px;top:41px;width:140px;height:75px;background:rgba(255,255,255,.82)"></div>
  <div class="abs" style="left:229px;top:41px;width:18px;height:16px;background:var(--orange)"></div>
  <div class="abs" style="left:40px;top:52px;font-size:38px;color:#fff;font-weight:400;line-height:1">01.</div>
  <div class="abs" style="left:117px;top:64px;font-size:20px;font-weight:700;color:#111">Part One</div>
</section>

<!-- 4 agenda -->
<section class="slide c1 r2">
  <div class="mark"><i></i>NEXORA</div>
  <div class="title" style="top:9px">Agenda</div>
  <div class="abs" style="left:0;top:41px;width:278px;height:88px;background:var(--orange)"></div>
  <div class="abs" style="left:141px;top:61px;width:.6px;height:42px;background:rgba(255,255,255,.7)"></div>
  <div class="abs" style="left:18px;top:51px;font-size:22px;color:#fff;line-height:1">01</div>
  <div class="abs" style="left:18px;top:86px;font-size:22px;color:#fff;line-height:1">02</div>
  <div class="abs" style="left:162px;top:51px;font-size:22px;color:#fff;line-height:1">03</div>
  <div class="abs" style="left:162px;top:86px;font-size:22px;color:#fff;line-height:1">04</div>
  <div class="abs" style="left:60px;top:50px;width:60px"><div style="font-size:5.5px;color:#fff">Content Title #01</div><div class="tw" style="margin-top:2px">simply dummy text of the printing and typesetting industry. Lorem ipsum has been</div></div>
  <div class="abs" style="left:60px;top:85px;width:60px"><div style="font-size:5.5px;color:#fff">Content Title #02</div><div class="tw" style="margin-top:2px">simply dummy text of the printing and typesetting industry. Lorem ipsum has been</div></div>
  <div class="abs" style="left:204px;top:50px;width:60px"><div style="font-size:5.5px;color:#fff">Content Title #03</div><div class="tw" style="margin-top:2px">simply dummy text of the printing and typesetting industry. Lorem ipsum has been</div></div>
  <div class="abs" style="left:204px;top:85px;width:60px"><div style="font-size:5.5px;color:#fff">Content Title #04</div><div class="tw" style="margin-top:2px">simply dummy text of the printing and typesetting industry. Lorem ipsum has been</div></div>
  <div class="foot"></div><div class="pg"><svg width="14" height="14"><polygon points="14,0 14,14 0,14" fill="#222"/></svg><span>4</span></div>
</section>

<!-- 5 agenda style -->
<section class="slide c2 r2" style="background:var(--dark)">
  <svg class="abs" style="left:0;top:0" width="278" height="156"><polygon points="0,0 143,0 70,156 0,156" fill="#f28a1e"/></svg>
  <div class="photo" role="img" aria-label="Orange toned photo of communication icons" style="left:0;top:0;width:110px;height:156px;background:linear-gradient(160deg,rgba(255,200,130,.5),rgba(244,122,0,0))"></div>
  <div class="abs" style="left:15px;top:71px;font-size:12px;font-weight:600;color:#fff">Agenda Style</div>
  <div class="abs" style="left:129px;top:43px;width:140px;height:15px">
    <div class="abs" style="left:0;top:0;width:28px;height:14px;background:var(--yellow);transform:skewX(-25deg)"></div>
    <div class="abs" style="left:6px;top:3px;font-size:5.5px;color:#fff">01</div>
    <div class="abs" style="left:22px;top:4px;width:118px;height:15px;background:#f4f4f4;padding:2px 12px"><div style="font-size:2.8px;color:#333;font-weight:700">Your Text Here</div><div style="font-size:2.8px;color:#555;margin-top:1px">Modern PowerPoint Presentation designed</div></div>
  </div>
  <div class="abs" style="left:119px;top:68px;width:150px;height:15px">
    <div class="abs" style="left:0;top:0;width:28px;height:14px;background:var(--orange);transform:skewX(-25deg)"></div>
    <div class="abs" style="left:6px;top:3px;font-size:5.5px;color:#fff">02</div>
    <div class="abs" style="left:22px;top:4px;width:128px;height:15px;background:#f4f4f4;padding:2px 12px"><div style="font-size:2.8px;color:#333;font-weight:700">Your Text Here</div><div style="font-size:2.8px;color:#555;margin-top:1px">Modern PowerPoint Presentation designed</div></div>
  </div>
  <div class="abs" style="left:109px;top:93px;width:160px;height:15px">
    <div class="abs" style="left:0;top:0;width:28px;height:14px;background:var(--yellow);transform:skewX(-25deg)"></div>
    <div class="abs" style="left:6px;top:3px;font-size:5.5px;color:#fff">03</div>
    <div class="abs" style="left:22px;top:4px;width:138px;height:15px;background:#f4f4f4;padding:2px 12px"><div style="font-size:2.8px;color:#333;font-weight:700">Your Text Here</div><div style="font-size:2.8px;color:#555;margin-top:1px">Modern PowerPoint Presentation designed</div></div>
  </div>
  <div class="abs" style="left:99px;top:118px;width:170px;height:15px">
    <div class="abs" style="left:0;top:0;width:28px;height:14px;background:var(--orange);transform:skewX(-25deg)"></div>
    <div class="abs" style="left:6px;top:3px;font-size:5.5px;color:#fff">04</div>
    <div class="abs" style="left:22px;top:4px;width:148px;height:15px;background:#f4f4f4;padding:2px 12px"><div style="font-size:2.8px;color:#333;font-weight:700">Your Text Here</div><div style="font-size:2.8px;color:#555;margin-top:1px">Modern PowerPoint Presentation designed</div></div>
  </div>
  <div class="pg"><svg width="14" height="14"><polygon points="14,0 14,14 0,14" fill="#222"/></svg><span>5</span></div>
</section>

<!-- 6 four points -->
<section class="slide c3 r2">
  <div class="mark"><i></i>NEXORA</div>
  <div class="title" style="top:9px">Lorem ipsum dolor</div>
  <div class="abs tw" style="left:13px;top:36px;width:250px;height:30px;background:var(--orange);padding:6px 8px;text-align:center">Lorem ipsum dolor sit amet, consectetuer adipiscing elit, sed diam nonummy nibh euismod tincidunt ut laoreet dolore magna aliquam erat volutpat. Ut wisi enim ad minim veniam, quis nostrud exerci tation ullamcorper suscipit lobortis nisl ut aliquip ex ea commodo consequat.</div>
  <div class="abs" style="left:13px;top:74px;width:118px">
    <div class="abs" style="left:0;top:8px;font-size:9px">01</div>
    <div class="abs" style="left:15px;top:0;width:103px;height:5px;background:#222;font-size:3px;color:#fff;padding:.6px 2px;font-weight:700">Your Text Here</div>
    <div class="abs t" style="left:15px;top:6px;width:103px;font-size:2.8px">You can simply impress your audience and add a unique zing and appeal to your Presentations. Get a modern PowerPoint Presentation that is beautifully designed.</div>
  </div>
  <div class="abs" style="left:140px;top:74px;width:118px">
    <div class="abs" style="left:0;top:8px;font-size:9px">03</div>
    <div class="abs" style="left:15px;top:0;width:103px;height:5px;background:#222;font-size:3px;color:#fff;padding:.6px 2px;font-weight:700">Your Text Here</div>
    <div class="abs t" style="left:15px;top:6px;width:103px;font-size:2.8px">You can simply impress your audience and add a unique zing and appeal to your Presentations. Get a modern PowerPoint Presentation that is beautifully designed.</div>
  </div>
  <div class="abs" style="left:13px;top:108px;width:118px">
    <div class="abs" style="left:0;top:8px;font-size:9px">02</div>
    <div class="abs" style="left:15px;top:0;width:103px;height:5px;background:#222;font-size:3px;color:#fff;padding:.6px 2px;font-weight:700">Your Text Here</div>
    <div class="abs t" style="left:15px;top:6px;width:103px;font-size:2.8px">You can simply impress your audience and add a unique zing and appeal to your Presentations. Get a modern PowerPoint Presentation that is beautifully designed.</div>
  </div>
  <div class="abs" style="left:140px;top:108px;width:118px">
    <div class="abs" style="left:0;top:8px;font-size:9px">04</div>
    <div class="abs" style="left:15px;top:0;width:103px;height:5px;background:#222;font-size:3px;color:#fff;padding:.6px 2px;font-weight:700">Your Text Here</div>
    <div class="abs t" style="left:15px;top:6px;width:103px;font-size:2.8px">You can simply impress your audience and add a unique zing and appeal to your Presentations. Get a modern PowerPoint Presentation that is beautifully designed.</div>
  </div>
  <div class="foot"></div><div class="pg"><svg width="14" height="14"><polygon points="14,0 14,14 0,14" fill="#222"/></svg><span>6</span></div>
</section>

<!-- 7 about -->
<section class="slide c1 r3">
  <div class="mark"><i></i>NEXORA</div>
  <div class="abs" style="left:0;top:17px;width:131px;height:121px;background:var(--orange)"></div>
  <div class="photo" role="img" aria-label="Photo of a hand typing on a blue lit keyboard" style="left:0;top:36px;width:138px;height:82px;background:linear-gradient(135deg,#9fb4d6,#3d4f8a 55%,#1c2552);box-shadow:2px 3px 5px rgba(0,0,0,.35)"></div>
  <div class="abs" style="left:155px;top:25px;font-size:8.5px;font-weight:600">A Few Words About</div>
  <div class="abs" style="left:155px;top:35px;font-size:12.5px;font-weight:600">Our Company</div>
  <div class="abs t" style="left:155px;top:59px;width:90px;text-align:justify">Lorem ipsum dolor sit amet, consectetur adipiscing elit, sed do eiusmod tempor incididunt ut labore et dolore magna aliqua. Lorem ipsum dolor sit amet, consectetur adipiscing elit, sed do eiusmod tempor incididunt ut labore et dolore magna aliqua. Ut enim ad minim veniam, quis nostrud exercitation ullamco laboris nisi ut aliquip. Lorem ipsum dolor sit amet, consectetur adipiscing elit, sed do eiusmod tempor incididunt ut labore et dolore magna aliqua.</div>
  <div class="foot"></div><div class="pg"><svg width="14" height="14"><polygon points="14,0 14,14 0,14" fill="#222"/></svg><span>7</span></div>
</section>

<!-- 8 statement -->
<section class="slide c2 r3">
  <div class="mark"><i></i>NEXORA</div>
  <div class="abs" style="left:0;top:14px;width:8px;height:70px;background:var(--orange)"></div>
  <div class="abs" style="left:15px;top:28px;font-size:9.5px;font-weight:700;line-height:1.3">Lorem ipsum<br>consectetur adipiscing elit,<br><span style="color:var(--orange)">eiusmod tempor</span> incididunt</div>
  <div class="photo" role="img" aria-label="Photo of a businessman holding a tablet with glowing icons" style="left:162px;top:17px;width:116px;height:59px;background:linear-gradient(135deg,#6d6d6d,#2d2d2d)"></div>
  <div class="abs" style="left:0;top:84px;width:162px;height:72px;background:#f1f1f1"></div>
  <div class="abs t" style="left:15px;top:96px;width:137px;text-align:justify">Lorem ipsum dolor sit amet, consectetur adipiscing elit, sed do eiusmod tempor incididunt ut labore et dolore magna aliqua. Lorem ipsum dolor sit amet, consectetur adipiscing elit, sed do eiusmod tempor incididunt ut labore et dolore magna aliqua. Ut enim ad minim veniam, quis nostrud exercitation ullamco laboris nisi ut aliquip Lorem ipsum dolor sit amet, consectetur adipiscing elit, sed do eiusmod tempor incididunt ut labore et dolore magna aliqua.</div>
  <div class="abs" style="left:162px;top:76px;width:116px;height:80px;background:var(--orange)"></div>
  <div class="abs tw" style="left:177px;top:94px;width:87px;text-align:justify">Lorem ipsum dolor sit amet, consectetur adipiscing elit, sed do eiusmod tempor incididunt ut labore et dolore magna aliqua. Lorem ipsum dolor sit amet, consectetur adipiscing elit, sed do eiusmod tempor incididunt ut labore et dolore magna aliqua.</div>
  <div class="pg"><svg width="14" height="14"><polygon points="14,0 14,14 0,14" fill="#222"/></svg><span>8</span></div>
</section>

<!-- 9 three features -->
<section class="slide c3 r3">
  <div class="mark"><i></i>NEXORA</div>
  <div class="title" style="top:15px">Lorem ipsum dolor</div>
  <div class="abs t" style="left:20px;top:44px;width:238px;text-align:center">Lorem ipsum dolor sit amet, consectetur adipiscing elit, sed do eiusmod tempor incididunt ut labore et dolore magna aliqua. Lorem ipsum dolor sit amet, consectetur adipiscing elit, sed do eiusmod tempor incididunt ut labore et dolore magna aliqua. Ut enim ad minim veniam, quis nostrud exercitation ullamco laboris nisi ut aliquip Lorem ipsum dolor sit amet, consectetur adipiscing elit, sed do eiusmod tempor incididunt ut labore et dolore magna aliqua.</div>
  <div class="abs" style="left:0;top:102px;width:278px;height:54px;background:var(--dark)"></div>
  <div class="abs" style="left:17px;top:73px;width:67px;height:66px;background:var(--orange);border-radius:8px"></div>
  <div class="abs" style="left:103px;top:73px;width:67px;height:66px;background:var(--orange);border-radius:8px"></div>
  <div class="abs" style="left:189px;top:73px;width:67px;height:66px;background:var(--orange);border-radius:8px"></div>
  <svg class="abs" style="left:43px;top:79px" width="14" height="20"><rect x="2" y="1" width="9" height="16" rx="1.5" fill="none" stroke="#fff" stroke-width="1.2"/><circle cx="6.5" cy="14.5" r=".9" fill="#fff"/></svg>
  <svg class="abs" style="left:128px;top:81px" width="18" height="14"><rect x="3" y="1" width="12" height="9" fill="none" stroke="#fff" stroke-width="1.2"/><line x1="0" y1="12" x2="18" y2="12" stroke="#fff" stroke-width="1.5"/></svg>
  <svg class="abs" style="left:214px;top:80px" width="18" height="16"><circle cx="10" cy="8" r="6.5" fill="none" stroke="#fff" stroke-width="1.2"/><rect x="1" y="5" width="7" height="8" fill="var(--orange)" stroke="#fff" stroke-width="1"/></svg>
  <div class="abs tw" style="left:22px;top:111px;width:57px;text-align:center;font-size:2.8px">Lorem ipsum dolor sit amet, consectetur adipiscing elit, sed do eiusmod tempor incididunt ut labore et dolore magna aliqua.</div>
  <div class="abs tw" style="left:108px;top:111px;width:57px;text-align:center;font-size:2.8px">Lorem ipsum dolor sit amet, consectetur adipiscing elit, sed do eiusmod tempor incididunt ut labore et dolore magna aliqua.</div>
  <div class="abs tw" style="left:194px;top:111px;width:57px;text-align:center;font-size:2.8px">Lorem ipsum dolor sit amet, consectetur adipiscing elit, sed do eiusmod tempor incididunt ut labore et dolore magna aliqua.</div>
  <div class="pg"><svg width="14" height="14"><polygon points="14,0 14,14 0,14" fill="#222"/></svg><span>9</span></div>
</section>

<!-- 10 icon list -->
<section class="slide c1 r4">
  <div class="mark"><i></i>NEXORA</div>
  <div class="abs t" style="left:12px;top:23px;width:66px;text-align:justify;font-size:3.6px">Lorem ipsum dolor sit amet, consectetur adipiscing elit, sed do eiusmod tempor incididunt ut labore et dolore magna aliqua. Lorem ipsum dolor sit amet, consectetur adipiscing elit, sed do eiusmod tempor incididunt ut labore et dolore magna aliqua. Ut enim ad minim veniam, quis nostrud exercitation ullamco laboris nisi ut aliquip Lorem ipsum dolor sit amet, consectetur adipiscing elit, sed do eiusmod tempor incididunt ut labore et dolore magna aliqua.</div>
  <div class="photo" role="img" aria-label="Orange toned photo of a person with technology words" style="left:91px;top:0;width:82px;height:148px;background:linear-gradient(160deg,#e59a55,#c96a1a)"></div>
  <div class="abs" style="left:91px;top:42px;width:82px;text-align:center;color:#fff;font-size:9px;font-weight:600;line-height:1.4">Lorem<br>ipsum dolor<br>sit amet,<br>consectetur<br>adipiscing<br>elit</div>
  <div class="ico" style="left:163px;top:28px;width:19px;height:19px;background:#fff;box-shadow:0 1px 3px rgba(0,0,0,.3)"><svg width="8" height="9"><circle cx="4" cy="3.5" r="3" fill="#333"/><rect x="2.6" y="6.5" width="2.8" height="2" fill="#333"/></svg></div>
  <div class="ico" style="left:163px;top:59px;width:19px;height:19px;background:#fff;box-shadow:0 1px 3px rgba(0,0,0,.3)"><svg width="9" height="9"><rect x=".5" y="1.5" width="8" height="7" fill="none" stroke="#333"/><line x1=".5" y1="3.5" x2="8.5" y2="3.5" stroke="#333"/></svg></div>
  <div class="ico" style="left:163px;top:90px;width:19px;height:19px;background:#fff;box-shadow:0 1px 3px rgba(0,0,0,.3)"><svg width="10" height="8"><rect x=".5" y="1.5" width="9" height="6" rx="1" fill="#333"/><circle cx="5" cy="4.5" r="1.8" fill="#fff"/></svg></div>
  <div class="ico" style="left:163px;top:121px;width:19px;height:19px;background:#fff;box-shadow:0 1px 3px rgba(0,0,0,.3)"><svg width="9" height="9"><circle cx="4.5" cy="3" r="2.2" fill="#333"/><path d="M0.5,9 Q4.5,3.5 8.5,9z" fill="#333"/></svg></div>
  <div class="abs t" style="left:188px;top:31px;width:78px;font-size:3px">Lorem ipsum dolor sit amet, consectetur adipiscing elit, sed do eiusmod tempor incididunt ut labore et dolore magna aliqua.</div>
  <div class="abs t" style="left:188px;top:62px;width:78px;font-size:3px">Lorem ipsum dolor sit amet, consectetur adipiscing elit, sed do eiusmod tempor incididunt ut labore et dolore magna aliqua.</div>
  <div class="abs t" style="left:188px;top:93px;width:78px;font-size:3px">Lorem ipsum dolor sit amet, consectetur adipiscing elit, sed do eiusmod tempor incididunt ut labore et dolore magna aliqua.</div>
  <div class="abs t" style="left:188px;top:124px;width:78px;font-size:3px">Lorem ipsum dolor sit amet, consectetur adipiscing elit, sed do eiusmod tempor incididunt ut labore et dolore magna aliqua.</div>
  <div class="foot"></div><div class="pg"><svg width="14" height="14"><polygon points="14,0 14,14 0,14" fill="#222"/></svg><span>10</span></div>
</section>

<!-- 11 text over photo -->
<section class="slide c2 r4">
  <div class="mark"><i></i>NEXORA</div>
  <div class="photo" role="img" aria-label="Blue photo of a hand with communication technology graphics" style="left:0;top:0;width:90px;height:148px;background:linear-gradient(160deg,#5b8fc4,#2f5f96)"></div>
  <div class="abs" style="left:90px;top:0;width:100px;height:148px;background:rgba(236,120,20,.92)"></div>
  <div class="abs" style="left:21px;top:20px;font-size:13px;color:#fff">Lorem ipsum dolor</div>
  <div class="abs tw" style="left:98px;top:40px;width:82px;text-align:justify">Lorem ipsum dolor sit amet, consectetur adipiscing elit, sed do eiusmod tempor incididunt ut labore et dolore magna aliqua. Lorem ipsum dolor sit amet, consectetur adipiscing elit, sed do eiusmod tempor incididunt ut labore et dolore magna aliqua.<br><br>Lorem ipsum dolor sit amet, consectetur adipiscing elit, sed do eiusmod tempor incididunt ut labore et dolore magna aliqua. Lorem ipsum dolor sit amet, consectetur adipiscing elit, sed do eiusmod tempor incididunt ut labore et dolore magna aliqua.</div>
  <div class="abs t" style="left:198px;top:40px;width:68px;text-align:justify;font-size:3.4px">Lorem ipsum dolor sit amet, consectetur adipiscing elit, sed do eiusmod tempor incididunt ut labore et dolore magna aliqua. Lorem ipsum dolor sit amet, consectetur adipiscing elit, sed do eiusmod tempor incididunt ut labore et dolore magna aliqua.<br><br>Lorem ipsum dolor sit amet, consectetur adipiscing elit, sed do eiusmod tempor incididunt ut labore et dolore magna aliqua. Lorem ipsum dolor sit amet, consectetur adipiscing elit, sed do eiusmod tempor incididunt ut labore et dolore magna aliqua.</div>
  <div class="foot"></div><div class="pg"><svg width="14" height="14"><polygon points="14,0 14,14 0,14" fill="#222"/></svg><span>11</span></div>
</section>

<!-- 12 stats -->
<section class="slide c3 r4">
  <div class="mark"><i></i>NEXORA</div>
  <div class="abs" style="left:164px;top:27px;width:114px;height:22px;background:var(--dark)"></div>
  <div class="photo" role="img" aria-label="Photo of a businessman touching an IT data diagram" style="left:164px;top:49px;width:114px;height:81px;background:linear-gradient(135deg,#3d5a88,#1d2c48)"></div>
  <div class="abs" style="left:10px;top:26px;font-size:10.5px;font-weight:600;color:var(--orange)">Lorem ipsum dolor sit amet</div>
  <div class="abs t" style="left:10px;top:45px;width:148px;text-align:justify">Lorem ipsum dolor sit amet, consectetuer adipiscing elit, sed diam nonummy nibh euismod tincidunt ut laoreet dolore magna aliquam erat volutpat. Ut wisi enim ad minim veniam, quis nostrud exerci tation ullamcorper suscipit lobortis nisl ut aliquip ex ea commodo consequat.</div>
  <div class="abs" style="left:10px;top:95px;width:46px;height:34px;border:1px solid var(--orange);text-align:center;padding-top:4px"><svg width="6" height="7"><circle cx="3" cy="2.5" r="2.3" fill="#333"/><rect x="2" y="4.5" width="2" height="2" fill="#333"/></svg><div style="font-size:5px;font-weight:700">1500</div><div class="t" style="font-size:2.8px">Lorem ipsum dolor</div></div>
  <div class="abs" style="left:62px;top:95px;width:46px;height:34px;border:1px solid var(--orange);text-align:center;padding-top:4px"><svg width="7" height="7"><circle cx="3.5" cy="3.5" r="2.6" fill="none" stroke="#333" stroke-width="1"/></svg><div style="font-size:5px;font-weight:700">900</div><div class="t" style="font-size:2.8px">Lorem ipsum dolor</div></div>
  <div class="abs" style="left:114px;top:95px;width:46px;height:34px;border:1px solid var(--orange);text-align:center;padding-top:4px"><svg width="6" height="7"><path d="M.5,.5H5.5L3,3.5L5.5,6.5H.5L3,3.5z" fill="#333"/></svg><div style="font-size:5px;font-weight:700">345</div><div class="t" style="font-size:2.8px">Lorem ipsum dolor</div></div>
  <div class="foot"></div><div class="pg"><svg width="14" height="14"><polygon points="14,0 14,14 0,14" fill="#222"/></svg><span>12</span></div>
</section>

<!-- 13 pricing table -->
<section class="slide c1 r5">
  <div class="mark"><i></i>NEXORA</div>
  <div class="title" style="top:17px">Lorem ipsum dolor</div>
  <div class="abs" style="left:90px;top:42px;width:50px;height:86px;background:#fff;box-shadow:0 0 4px rgba(0,0,0,.35)"></div>
  <div class="abs" style="left:41px;top:44px;width:207px;font-size:3.5px">
    <div style="display:grid;grid-template-columns:49px 50px 54px 54px;height:12px;align-items:center;font-weight:700;text-align:center;border-bottom:.6px solid var(--line)"><span></span><span>Basic</span><span>Pro</span><span>Ultimate</span></div>
    <div style="display:grid;grid-template-columns:49px 50px 54px 54px;height:12.5px;align-items:center;text-align:center;border-bottom:.6px solid var(--line);font-size:3px"><span style="text-align:left">Lorem ipsum dolor</span><span>25$</span><span>65$</span><span>100$</span></div>
    <div style="display:grid;grid-template-columns:49px 50px 54px 54px;height:12.5px;align-items:center;text-align:center;border-bottom:.6px solid var(--line);font-size:3px"><span style="text-align:left">Lorem ipsum dolor</span><span>03</span><span>03</span><span>Ultimate</span></div>
    <div style="display:grid;grid-template-columns:49px 50px 54px 54px;height:12.5px;align-items:center;text-align:center;border-bottom:.6px solid var(--line);font-size:3px"><span style="text-align:left">Lorem ipsum dolor</span><span>512</span><span>512</span><span>Ultimate</span></div>
    <div style="display:grid;grid-template-columns:49px 50px 54px 54px;height:12.5px;align-items:center;text-align:center;border-bottom:.6px solid var(--line);font-size:3px"><span style="text-align:left">Lorem ipsum dolor</span><span>13</span><span>13</span><span>Ultimate</span></div>
    <div style="display:grid;grid-template-columns:49px 50px 54px 54px;height:12.5px;align-items:center;text-align:center;border-bottom:.6px solid var(--line);font-size:3px"><span style="text-align:left">Lorem ipsum dolor</span><span>394</span><span>394</span><span>Ultimate</span></div>
  </div>
  <div class="foot"></div><div class="pg"><svg width="14" height="14"><polygon points="14,0 14,14 0,14" fill="#222"/></svg><span>13</span></div>
</section>

<!-- 14 timeline -->
<section class="slide c2 r5">
  <div class="mark"><i></i>NEXORA</div>
  <div class="title" style="top:17px">Lorem ipsum dolor</div>
  <div class="abs t" style="left:80px;top:48px;width:40px;font-size:2.8px">● Simply Presentation<br>Modern PowerPoint<br>Modern PowerPoint<br>PowerPoint Presentation</div>
  <div class="abs t" style="left:159px;top:48px;width:40px;font-size:2.8px">● Simply Presentation<br>Modern PowerPoint<br>Modern PowerPoint<br>PowerPoint Presentation</div>
  <div class="abs" style="left:39px;top:86px;width:198px;height:7px;display:flex;font-size:3.2px;color:#fff;font-weight:700">
    <span style="flex:1;background:var(--orange);text-align:center;line-height:7px">2015</span>
    <span style="flex:1;background:#9a9a9a;text-align:center;line-height:7px">2016</span>
    <span style="flex:1;background:var(--orange);text-align:center;line-height:7px">2017</span>
    <span style="flex:1;background:#9a9a9a;text-align:center;line-height:7px">2018</span>
    <span style="flex:1;background:var(--orange);text-align:center;line-height:7px">2019</span>
  </div>
  <div class="abs" style="left:18px;top:81px;width:18px;height:17px;border:.8px solid var(--orange);display:flex;align-items:center;justify-content:center"><svg width="7" height="8"><circle cx="3.5" cy="3" r="2.6" fill="var(--orange)"/><rect x="2.3" y="5.6" width="2.4" height="2" fill="var(--orange)"/></svg></div>
  <div class="abs" style="left:239px;top:81px;width:19px;height:18px;background:var(--orange);display:flex;align-items:center;justify-content:center"><svg width="9" height="9"><path d="M1,8L8,1M5,1H8V4" stroke="#fff" stroke-width="1.2" fill="none"/></svg></div>
  <div class="abs t" style="left:40px;top:104px;width:40px;font-size:2.8px">● Simply Presentation<br>Modern PowerPoint<br>Modern PowerPoint<br>PowerPoint Presentation</div>
  <div class="abs t" style="left:119px;top:104px;width:40px;font-size:2.8px">● Simply Presentation<br>Modern PowerPoint<br>Modern PowerPoint<br>PowerPoint Presentation</div>
  <div class="abs t" style="left:198px;top:104px;width:40px;font-size:2.8px">● Simply Presentation<br>Modern PowerPoint<br>Modern PowerPoint<br>PowerPoint Presentation</div>
  <div class="foot"></div><div class="pg"><svg width="14" height="14"><polygon points="14,0 14,14 0,14" fill="#222"/></svg><span>14</span></div>
</section>

<!-- 15 cycle -->
<section class="slide c3 r5">
  <div class="mark"><i></i>NEXORA</div>
  <div class="title" style="top:15px">Lorem ipsum dolor</div>
  <svg class="abs" style="left:0;top:0" width="278" height="156">
    <circle cx="139" cy="89" r="36" fill="none" stroke="#1f2a4a" stroke-width="1.5"/>
    <circle cx="139" cy="89" r="17" fill="#333"/>
    <circle cx="139" cy="89" r="8" fill="none" stroke="#fff" stroke-width="1.3"/>
    <circle cx="139" cy="89" r="3.5" fill="none" stroke="#fff" stroke-width="1.3"/>
    <g fill="var(--orange)">
      <circle cx="121" cy="58" r="9"/><circle cx="157" cy="58" r="9"/>
      <circle cx="103" cy="89" r="9"/><circle cx="175" cy="89" r="9"/>
      <circle cx="121" cy="120" r="9"/><circle cx="157" cy="120" r="9"/>
    </g>
  </svg>
  <div class="abs t" style="left:40px;top:38px;width:68px;text-align:right;font-size:2.8px"><b style="color:#333">Add Text</b><br>Get a modern PowerPoint Presentation that is beautifully designed. Easy to change colors, photos.</div>
  <div class="abs t" style="left:177px;top:38px;width:68px;font-size:2.8px"><b style="color:#333">Add Text</b><br>Get a modern PowerPoint Presentation that is beautifully designed. Easy to change colors, photos.</div>
  <div class="abs t" style="left:23px;top:77px;width:68px;text-align:right;font-size:2.8px"><b style="color:#333">Add Text</b><br>Get a modern PowerPoint Presentation that is beautifully designed. Easy to change colors, photos.</div>
  <div class="abs t" style="left:193px;top:77px;width:68px;font-size:2.8px"><b style="color:#333">Add Text</b><br>Get a modern PowerPoint Presentation that is beautifully designed. Easy to change colors, photos.</div>
  <div class="abs t" style="left:40px;top:116px;width:68px;text-align:right;font-size:2.8px"><b style="color:#333">Add Text</b><br>Get a modern PowerPoint Presentation that is beautifully designed. Easy to change colors, photos.</div>
  <div class="abs t" style="left:177px;top:116px;width:68px;font-size:2.8px"><b style="color:#333">Add Text</b><br>Get a modern PowerPoint Presentation that is beautifully designed. Easy to change colors, photos.</div>
  <div class="foot"></div><div class="pg"><svg width="14" height="14"><polygon points="14,0 14,14 0,14" fill="#222"/></svg><span>15</span></div>
</section>

<!-- 17 four boxes -->
<section class="slide c1 r6">
  <div class="mark"><i></i>NEXORA</div>
  <div class="photo" role="img" aria-label="Cyan illustration of a hand touching a network of devices and users" style="left:0;top:0;width:117px;height:148px;background:linear-gradient(160deg,#3fb6d6,#0d88b8)"></div>
  <div class="abs" style="left:131px;top:17px;font-size:13.5px">Lorem ipsum dolor</div>
  <div class="abs" style="left:132px;top:41px;width:61px">
    <div style="background:var(--orange);color:#fff;font-size:3.3px;text-align:center;padding:1.5px 0">Your Contents Here</div>
    <div class="t" style="padding:3px 6px;text-align:justify;font-size:2.9px">Lorem ipsum dolor sit amet, consectetur adipiscing elit, sed do eiusmod tempor incididunt ut labore et dolore magna aliqua. Lorem ipsum dolor sit amet, consectetur adipiscing elit.</div>
  </div>
  <div class="abs" style="left:197px;top:41px;width:61px">
    <div style="background:var(--orange);color:#fff;font-size:3.3px;text-align:center;padding:1.5px 0">Your Contents Here</div>
    <div class="t" style="padding:3px 6px;text-align:justify;font-size:2.9px">Lorem ipsum dolor sit amet, consectetur adipiscing elit, sed do eiusmod tempor incididunt ut labore et dolore magna aliqua. Lorem ipsum dolor sit amet, consectetur adipiscing elit.</div>
  </div>
  <div class="abs" style="left:132px;top:94px;width:61px">
    <div style="background:var(--orange);color:#fff;font-size:3.3px;text-align:center;padding:1.5px 0">Your Contents Here</div>
    <div class="t" style="padding:3px 6px;text-align:justify;font-size:2.9px">Lorem ipsum dolor sit amet, consectetur adipiscing elit, sed do eiusmod tempor incididunt ut labore et dolore magna aliqua. Lorem ipsum dolor sit amet, consectetur adipiscing elit.</div>
  </div>
  <div class="abs" style="left:197px;top:94px;width:61px">
    <div style="background:var(--orange);color:#fff;font-size:3.3px;text-align:center;padding:1.5px 0">Your Contents Here</div>
    <div class="t" style="padding:3px 6px;text-align:justify;font-size:2.9px">Lorem ipsum dolor sit amet, consectetur adipiscing elit, sed do eiusmod tempor incididunt ut labore et dolore magna aliqua. Lorem ipsum dolor sit amet, consectetur adipiscing elit.</div>
  </div>
  <div class="foot"></div><div class="pg"><svg width="14" height="14"><polygon points="14,0 14,14 0,14" fill="#222"/></svg><span>17</span></div>
</section>

<!-- 16 process -->
<section class="slide c2 r6">
  <div class="mark"><i></i>NEXORA</div>
  <div class="title" style="top:5px">Lorem ipsum dolor</div>
  <div class="abs t" style="left:55px;top:33px;width:168px;text-align:center;font-size:2.9px">Lorem ipsum dolor sit amet, consectetur adipiscing elit, sed do eiusmod tempor incididunt ut labore et dolore magna aliqua. Lorem ipsum dolor sit amet, consectetur adipiscing elit, sed do eiusmod tempor incididunt ut labore et dolore magna aliqua.</div>
  <svg class="abs" style="left:0;top:0" width="278" height="156">
    <path d="M126,71H154M118,79V99M162,79V99M126,107H154" stroke="var(--orange)" stroke-width="1"/>
    <rect x="110" y="63" width="16" height="16" fill="#fff" stroke="var(--orange)"/>
    <rect x="154" y="63" width="16" height="16" fill="#fff" stroke="#333"/>
    <rect x="110" y="99" width="16" height="16" fill="#fff" stroke="var(--orange)"/>
    <rect x="154" y="99" width="16" height="16" fill="#fff" stroke="#333"/>
    <path d="M114,66H122V69A4,4 0 0 1 114,69Z M117,73H119V75H115.5V76.5H120.5V75H119" fill="var(--orange)"/>
    <path d="M158,76V71M161,76V68M164,76V70M167,76V66" stroke="#333" stroke-width="1.4"/>
    <circle cx="118" cy="106" r="3" fill="var(--orange)"/><rect x="116.8" y="109" width="2.4" height="2" fill="var(--orange)"/>
    <circle cx="162" cy="107" r="5" fill="#333"/><path d="M162,107V102A5,5 0 0 1 167,107Z" fill="#fff"/>
  </svg>
  <div class="abs t" style="left:15px;top:64px;width:92px;text-align:center;font-size:2.8px"><b style="color:#333;font-size:3.3px">Your Contents Here</b><br>You can simply impress your audience and add a unique zing and appeal to your Presentations. Easy to change colors, photos.</div>
  <div class="abs t" style="left:174px;top:64px;width:92px;font-size:2.8px"><b style="color:#333;font-size:3.3px">Your Contents Here</b><br>You can simply impress your audience and add a unique zing and appeal to your Presentations. Easy to change colors, photos.</div>
  <div class="abs t" style="left:15px;top:101px;width:92px;text-align:center;font-size:2.8px"><b style="color:#333;font-size:3.3px">Your Contents Here</b><br>You can simply impress your audience and add a unique zing and appeal to your Presentations. Easy to change colors, photos.</div>
  <div class="abs t" style="left:174px;top:101px;width:92px;font-size:2.8px"><b style="color:#333;font-size:3.3px">Your Contents Here</b><br>You can simply impress your audience and add a unique zing and appeal to your Presentations. Easy to change colors, photos.</div>
  <div class="foot"></div><div class="pg"><svg width="14" height="14"><polygon points="14,0 14,14 0,14" fill="#222"/></svg><span>16</span></div>
</section>

<!-- 18 org chart -->
<section class="slide c3 r6">
  <div class="mark"><i></i>NEXORA</div>
  <div class="title" style="top:5px">Lorem ipsum dolor</div>
  <svg class="abs" style="left:0;top:0" width="278" height="156">
    <g stroke="#999" stroke-width=".5" fill="none">
      <path d="M137,43V48M53,51V48H221V51"/>
      <path d="M31,67V129H45M31,81H45M31,105H45"/>
      <path d="M114,67V129H128M114,81H128M114,105H128"/>
      <path d="M198,67V129H212M198,81H212M198,105H212"/>
    </g>
  </svg>
  <div class="abs" style="left:107px;top:28px;width:59px;height:15px;background:var(--orange);color:#fff;text-align:center;font-size:3.3px;padding-top:2px">FIRST / LAST NAME<div style="font-size:2.6px;opacity:.85;margin-top:2px">Position</div></div>
  <div class="abs" style="left:24px;top:51px;width:59px;height:16px;background:var(--orange);color:#fff;text-align:center;font-size:3.3px;padding-top:2px">FIRST / LAST NAME<div style="font-size:2.6px;opacity:.85;margin-top:2px">Position</div></div>
  <div class="abs" style="left:107px;top:51px;width:59px;height:16px;background:var(--orange);color:#fff;text-align:center;font-size:3.3px;padding-top:2px">FIRST / LAST NAME<div style="font-size:2.6px;opacity:.85;margin-top:2px">Position</div></div>
  <div class="abs" style="left:191px;top:51px;width:59px;height:16px;background:var(--orange);color:#fff;text-align:center;font-size:3.3px;padding-top:2px">FIRST / LAST NAME<div style="font-size:2.6px;opacity:.85;margin-top:2px">Position</div></div>
  <div class="abs" style="left:45px;top:75px;width:40px;height:13px;border:.5px solid #bbb;text-align:center;font-size:2.8px;color:#888;padding-top:2px">FIRST / LAST NAME<div style="background:#eee;font-size:2.2px;margin:2px 4px 0">Position</div></div>
  <div class="abs" style="left:45px;top:98px;width:40px;height:13px;border:.5px solid #bbb;text-align:center;font-size:2.8px;color:#888;padding-top:2px">FIRST / LAST NAME<div style="background:#eee;font-size:2.2px;margin:2px 4px 0">Position</div></div>
  <div class="abs" style="left:45px;top:122px;width:40px;height:13px;border:.5px solid #bbb;text-align:center;font-size:2.8px;color:#888;padding-top:2px">FIRST / LAST NAME<div style="background:#eee;font-size:2.2px;margin:2px 4px 0">Position</div></div>
  <div class="abs" style="left:128px;top:75px;width:40px;height:13px;border:.5px solid #bbb;text-align:center;font-size:2.8px;color:#888;padding-top:2px">FIRST / LAST NAME<div style="background:#eee;font-size:2.2px;margin:2px 4px 0">Position</div></div>
  <div class="abs" style="left:128px;top:98px;width:40px;height:13px;border:.5px solid #bbb;text-align:center;font-size:2.8px;color:#888;padding-top:2px">FIRST / LAST NAME<div style="background:#eee;font-size:2.2px;margin:2px 4px 0">Position</div></div>
  <div class="abs" style="left:128px;top:122px;width:40px;height:13px;border:.5px solid #bbb;text-align:center;font-size:2.8px;color:#888;padding-top:2px">FIRST / LAST NAME<div style="background:#eee;font-size:2.2px;margin:2px 4px 0">Position</div></div>
  <div class="abs" style="left:212px;top:75px;width:40px;height:13px;border:.5px solid #bbb;text-align:center;font-size:2.8px;color:#888;padding-top:2px">FIRST / LAST NAME<div style="background:#eee;font-size:2.2px;margin:2px 4px 0">Position</div></div>
  <div class="abs" style="left:212px;top:98px;width:40px;height:13px;border:.5px solid #bbb;text-align:center;font-size:2.8px;color:#888;padding-top:2px">FIRST / LAST NAME<div style="background:#eee;font-size:2.2px;margin:2px 4px 0">Position</div></div>
  <div class="abs" style="left:212px;top:122px;width:40px;height:13px;border:.5px solid #bbb;text-align:center;font-size:2.8px;color:#888;padding-top:2px">FIRST / LAST NAME<div style="background:#eee;font-size:2.2px;margin:2px 4px 0">Position</div></div>
  <div class="foot"></div><div class="pg"><svg width="14" height="14"><polygon points="14,0 14,14 0,14" fill="#222"/></svg><span>18</span></div>
</section>

<!-- 19 images & contents -->
<section class="slide c1 r7">
  <div class="photo" role="img" aria-label="Orange toned photo of an office desk with computers" style="left:0;top:0;width:278px;height:82px;background:linear-gradient(180deg,#f0a04a,#ec8a22)"></div>
  <div class="abs" style="left:0;top:26px;width:278px;text-align:center;font-size:12.5px;color:#fff">Images &amp; Contents</div>
  <div class="abs tw" style="left:38px;top:44px;width:202px;text-align:center;font-size:3.5px">Lorem ipsum dolor sit amet, consectetur adipiscing elit, sed do eiusmod tempor incididunt ut labore et dolore magna aliqua. Lorem ipsum dolor sit amet, consectetur adipiscing elit, sed do eiusmod tempor incididunt ut labore et dolore magna aliqua.</div>
  <div class="photo" role="img" aria-label="Illustration of a black smartphone with a blank screen" style="left:17px;top:54px;width:54px;height:97px;border-radius:5px;background:#2a2a2a"></div>
  <div class="abs" style="left:21px;top:61px;width:46px;height:80px;background:#fff"></div>
  <div class="ico" style="left:93px;top:97px;width:16px;height:16px;background:var(--orange)"><svg width="7" height="6"><rect y="1" width="7" height="5" rx="1" fill="#fff"/></svg></div>
  <div class="ico" style="left:180px;top:97px;width:16px;height:16px;background:#333"><svg width="7" height="7"><path d="M1,1H6V6H1Z" fill="#fff"/></svg></div>
  <div class="ico" style="left:93px;top:126px;width:16px;height:16px;background:#333"><svg width="7" height="6"><rect y="1" width="7" height="5" rx="1" fill="#fff"/><circle cx="3.5" cy="3.5" r="1.3" fill="#333"/></svg></div>
  <div class="ico" style="left:180px;top:126px;width:16px;height:16px;background:var(--orange)"><svg width="7" height="6"><path d="M0,1H3.3V6H0ZM3.7,1H7V6H3.7Z" fill="#fff"/></svg></div>
  <div class="abs t" style="left:114px;top:96px;width:60px;font-size:2.8px"><b style="color:#333">Contents Title</b><br>You can simply impress your audience and add a unique zing and appeal to your Presentations. Easy to change colors, photos and Text.</div>
  <div class="abs t" style="left:201px;top:96px;width:60px;font-size:2.8px"><b style="color:#333">Contents Title</b><br>You can simply impress your audience and add a unique zing and appeal to your Presentations. Easy to change colors, photos and Text.</div>
  <div class="abs t" style="left:114px;top:125px;width:60px;font-size:2.8px"><b style="color:#333">Contents Title</b><br>You can simply impress your audience and add a unique zing and appeal to your Presentations. Easy to change colors, photos and Text.</div>
  <div class="abs t" style="left:201px;top:125px;width:60px;font-size:2.8px"><b style="color:#333">Contents Title</b><br>You can simply impress your audience and add a unique zing and appeal to your Presentations. Easy to change colors, photos and Text.</div>
  <div class="foot"></div><div class="pg"><svg width="14" height="14"><polygon points="14,0 14,14 0,14" fill="#222"/></svg><span>19</span></div>
</section>

<!-- 20 world map -->
<section class="slide c2 r7">
  <div class="mark"><i></i>NEXORA</div>
  <div class="title" style="top:5px">Lorem ipsum dolor</div>
  <div class="photo" role="img" aria-label="Grey world map with orange location highlights in South America and East Asia" style="left:33px;top:30px;width:204px;height:111px;border-radius:30px;background:radial-gradient(ellipse at center,#c4c4c4,#dcdcdc 70%,#fff)"></div>
  <div class="foot"></div><div class="pg"><svg width="14" height="14"><polygon points="14,0 14,14 0,14" fill="#222"/></svg><span>20</span></div>
</section>

<!-- 21 contact -->
<section class="slide c3 r7">
  <div class="mark"><i></i>NEXORA</div>
  <svg class="abs" style="left:0;top:0" width="278" height="156">
    <path d="M147,89 L120,132 A52,52 0 1 1 120,46 Z" fill="var(--orange)"/>
    <circle cx="78" cy="89" r="52" fill="var(--orange)"/>
  </svg>
  <div class="abs" style="left:10px;top:70px;width:130px;text-align:center;font-size:24px;font-weight:800;color:#fff;letter-spacing:1px;line-height:1">NEXORA</div>
  <div class="abs" style="left:10px;top:98px;width:130px;text-align:center;font-size:13px;font-weight:700;color:#fff">Get in Touch</div>
  <svg class="abs" style="left:185px;top:36px" width="12" height="12"><path d="M2,1L4.5,1L5.5,4L4,5Q5,8 8,9L9,7.5L11.5,8.5L11.5,11Q5,11.5 1,4Z" fill="var(--orange)"/></svg>
  <svg class="abs" style="left:185px;top:62px" width="12" height="12"><circle cx="6" cy="6" r="5.2" fill="none" stroke="var(--orange)"/><ellipse cx="6" cy="6" rx="2.3" ry="5.2" fill="none" stroke="var(--orange)"/><path d="M.8,6H11.2" stroke="var(--orange)"/></svg>
  <svg class="abs" style="left:185px;top:89px" width="13" height="10"><rect x=".5" y=".5" width="12" height="9" fill="var(--orange)"/><path d="M.5,.5L6.5,5.5L12.5,.5" fill="none" stroke="#fff"/></svg>
  <svg class="abs" style="left:187px;top:113px" width="10" height="14"><path d="M5,13.5Q0,7 0,5A5,5 0 0 1 10,5Q10,7 5,13.5Z" fill="var(--orange)"/><circle cx="5" cy="5" r="1.8" fill="#fff"/></svg>
  <div class="abs" style="left:203px;top:38px;font-size:4.5px">555.010.2040</div>
  <div class="abs" style="left:203px;top:65px;font-size:4.5px">www.nexora-example.com</div>
  <div class="abs" style="left:206px;top:91px;font-size:4.5px">hello@nexora-example.com</div>
  <div class="abs" style="left:202px;top:114px;font-size:4.5px;text-align:center;line-height:1.3">Here to write your,<br>Company adress</div>
  <div class="foot"></div><div class="pg"><svg width="14" height="14"><polygon points="14,0 14,14 0,14" fill="#222"/></svg><span>21</span></div>
</section>

</div>
</body>
</html>
```